family doctor wants look of political campaign type ad

We would like an advertisement for a family doctor that mimics a political campaign in the US. I have uploaded a mailer that has gone out. We would like similar information. Our logo, the doctor's photo, and contact page (we want map) are also uploaded.
We would like an advertisement that is for a full page in a magazine. We would also like a smaller version (half page) for other newspaper, etc in color and grayscale/b&w - we would start a new design project with selected designer for half page ad.

Target Market(s)

all adults

Industry/Entity Type

Healthcare

Requirements
Must have
• the look of a political campagn
• photo, logo, map to location, address, phone, website address, insurance ID numbers, hours of operation

```html
<!DOCTYPE html>
<html lang="en">
<head>
<meta charset="utf-8">
<title>Harborline Medical Group – Dr. Daniel R. Whitmore</title>
<link href="https://fonts.googleapis.com/css2?family=Russo+One&family=Montserrat:wght@600;700&display=swap" rel="stylesheet">
<style>
  :root{
    --navy:#232f5c;
    --red:#c0282a;
    --paper:#ffffff;
    --paper-shade:#f1f1f3;
    --map-green:#dfe6c4;
  }
  *{margin:0;padding:0;box-sizing:border-box;}
  html,body{width:1200px;height:1200px;overflow:hidden;background:var(--paper);}
  .ad{
    position:absolute;left:148px;top:0;width:908px;height:1200px;overflow:hidden;
    background:radial-gradient(ellipse at 40% 55%, var(--paper) 40%, var(--paper-shade) 100%);
    font-family:"Russo One",sans-serif;
  }
  .flag{position:absolute;left:0;top:0;width:908px;height:320px;}
  .vote-badge{
    position:absolute;left:574px;top:36px;width:276px;height:276px;border-radius:50%;
    background:var(--paper);border:14px solid var(--red);
    box-shadow:0 4px 10px rgba(0,0,0,.25);
    display:flex;flex-direction:column;align-items:center;justify-content:center;gap:12px;
  }
  .vote-badge__word{color:var(--navy);font-size:62px;letter-spacing:2px;line-height:1;}
  .vote-badge__name{color:var(--red);font-size:18px;text-align:center;line-height:1.25;}
  .vote-badge__mark{width:44px;height:44px;background:var(--red);}
  .headline{
    position:absolute;left:56px;top:346px;transform:rotate(-4deg);transform-origin:left top;
    color:var(--navy);font-weight:400;white-space:nowrap;
  }
  .headline__first{color:var(--red);font-size:66px;line-height:1;letter-spacing:1px;}
  .headline__last{font-size:104px;line-height:1;letter-spacing:1px;}
  .headline__cred{font-size:28px;letter-spacing:1px;margin-left:6px;}
  .tagline{
    position:absolute;left:60px;top:560px;transform:rotate(-6deg);transform-origin:left top;
    font-size:40px;line-height:1;color:var(--red);white-space:nowrap;
  }
  .tagline .navy{color:var(--navy);}
  .stars{position:absolute;left:70px;top:578px;width:560px;height:190px;}
  .pitch{position:absolute;left:96px;top:790px;transform:rotate(-12deg);transform-origin:left top;text-align:center;line-height:.95;}
  .pitch__lead{color:var(--red);font-size:42px;}
  .pitch__main{color:var(--navy);font-size:60px;}
  .portrait{
    position:absolute;left:640px;top:528px;width:464px;height:464px;border-radius:50%;
    background:radial-gradient(circle at 50% 35%, #d9b79a 0 24%, #6b5a4c 40%, #2b2b2d 60%);
  }
  .cta{position:absolute;left:56px;top:1004px;}
  .cta__call{color:var(--red);font-size:52px;line-height:1;}
  .cta__phone{color:var(--navy);font-size:64px;line-height:1;margin-top:14px;margin-left:16px;}
  .address{
    position:absolute;left:0;width:908px;top:1136px;text-align:center;
    font-family:"Montserrat",sans-serif;font-weight:700;font-size:17px;color:var(--navy);
  }
  .map{
    position:absolute;left:572px;top:1006px;width:266px;height:114px;border-radius:6px;
    background:linear-gradient(120deg,var(--paper) 0%,var(--map-green) 45%,var(--map-green) 70%,var(--paper) 100%);
  }
</style>
</head>
<body>
<main class="ad">
  <svg class="flag" viewBox="0 0 908 320" role="img" aria-label="Waving American flag banner">
    <defs>
      <linearGradient id="flagTone" x1="0" y1="0" x2="1" y2="0">
        <stop offset="0" stop-color="#232f5c"/>
        <stop offset=".42" stop-color="#2a3667"/>
        <stop offset=".48" stop-color="#c0282a"/>
        <stop offset="1" stop-color="#d84a46"/>
      </linearGradient>
    </defs>
    <path d="M0 0H908V110C760 120 600 150 460 200 300 240 120 260 0 312Z" fill="url(#flagTone)"/>
  </svg>

  <div class="vote-badge">
    <div class="vote-badge__word">VOTE</div>
    <div class="vote-badge__mark"></div>
    <div class="vote-badge__name">Harborline<br>Medical Group</div>
  </div>

  <h1 class="headline">
    <div class="headline__first">DR. DANIEL R.</div>
    <div class="headline__last">WHITMORE<span class="headline__cred">, MD, MS</span></div>
  </h1>

  <p class="tagline">FOR <span class="navy">YOUR</span> FAMILY'S HEALTHCARE</p>

  <svg class="stars" viewBox="0 0 560 190" aria-hidden="true">
    <defs>
      <polygon id="star" points="0,-46 13,-14 46,-14 20,6 29,40 0,20 -29,40 -20,6 -46,-14 -13,-14" fill="#232f5c"/>
    </defs>
    <use href="#star" x="56" y="136"/>
    <use href="#star" x="164" y="114"/>
    <use href="#star" x="272" y="92"/>
    <use href="#star" x="380" y="70"/>
    <use href="#star" x="488" y="48"/>
  </svg>

  <div class="pitch">
    <div class="pitch__lead">I WANT TO BE YOUR</div>
    <div class="pitch__main">PRIMARY CARE<br>PHYSICIAN</div>
  </div>

  <div class="portrait" role="img" aria-label="Portrait photo of the doctor in a dark suit and tie"></div>

  <div class="cta">
    <div class="cta__call">ELECT US TODAY!</div>
    <div class="cta__phone">(949)555-0148</div>
  </div>

  <div class="map" role="img" aria-label="Location map showing the freeway, parkway and the clinic marker"></div>

  <p class="address">41180 Canyon Parkway, Canyon Medical Plaza, Suite 210, Mission Viejo, CA 92691</p>
</main>
</body>
</html>
```